Lumora Flow Collective Business Cards

I need business cards for staff in a new startup. Our company name is MorvaLeap - we train Tai Chi teachers. But our biggest project is called Lumora Flow Collective - a federal project to put together free Tai Chi classes for Vets all across America. It's a young company, with a spirit of excitement, passion, a desire to do good for others (our Vets) and a modern style and sensibility. In other words, not old-fashioned Asian martial arts theme, but something new.

Industry/Entity Type

Health And Wellness

Contact Information for Business Card

The topic is ancient healing, but the company is the Quibbletons - so I'd like a card design that captures that.

Font styles to use
Sans Serif

Colors

Designer to choose colors to be used in the design.

Requirements
Nice to have
• I've got two logos - one for the company and one for the project. I want to see if we can incorporate them both without it becoming too busy.
Should not have
• Overly old-fashioned yin-yang themes.

```html
<!DOCTYPE html>
<html lang="en">
<head>
<meta charset="utf-8">
<title>Lumora Flow Collective – Business Cards</title>
<link href="https://fonts.googleapis.com/css2?family=Lato:wght@400;700&display=swap" rel="stylesheet">
<style>
  :root {
    --bg: #2a2a2c;
    --card-dark: #1c1c1e;
    --card-light: #ffffff;
    --navy: #2f2d72;
    --red: #e8212e;
    --gold: #f2e27a;
    --text-grey: #4a4a4f;
    --white: #ffffff;
  }
  * { margin: 0; padding: 0; box-sizing: border-box; }
  html, body { width: 1200px; height: 960px; overflow: hidden; }
  body {
    background: var(--bg);
    font-family: "Lato", sans-serif;
    position: relative;
  }
  .card {
    position: absolute;
    left: 250px;
    width: 700px;
    height: 400px;
    overflow: hidden;
  }
  /* Front */
  .card--front {
    top: 60px;
    background: var(--card-dark);
  }
  .front-brand {
    position: absolute;
    left: 0; right: 0; top: 130px;
    display: flex; justify-content: center; align-items: center; gap: 18px;
  }
  .front-brand__dot {
    width: 56px; height: 56px; border-radius: 50%;
    background: var(--red);
  }
  .front-brand__name {
    font-size: 44px; font-weight: 700; color: var(--red); letter-spacing: 1px;
  }
  .front-url {
    position: absolute; left: 0; right: 0; top: 300px;
    text-align: center; color: var(--white);
    font-size: 17px; letter-spacing: 5px;
  }
  /* Back */
  .card--back {
    top: 500px;
    background: var(--card-light);
  }
  .back-wave { position: absolute; inset: 0; }
  .holder {
    position: absolute; right: 50px; top: 38px;
    text-align: right; color: var(--white);
  }
  .holder__name { font-size: 26px; font-weight: 700; letter-spacing: 0.5px; }
  .holder__title { font-size: 14px; font-weight: 700; letter-spacing: 1px; }
  .back-brand {
    position: absolute; left: 48px; top: 220px;
    display: flex; align-items: center; gap: 14px;
  }
  .back-brand__dot {
    width: 44px; height: 44px; border-radius: 50%;
    background: var(--navy);
  }
  .back-brand__name {
    font-size: 26px; font-weight: 700; color: var(--navy);
  }
  .contacts {
    position: absolute; left: 48px; top: 296px;
    list-style: none; color: var(--text-grey); font-size: 16px;
  }
  .contacts li { display: flex; align-items: center; gap: 10px; line-height: 23px; }
  .contacts svg { width: 14px; height: 14px; fill: var(--navy); }
  .address {
    position: absolute; right: 48px; top: 186px;
    text-align: right; color: var(--text-grey); font-size: 16px; line-height: 23px;
  }
</style>
</head>
<body>
  <section class="card card--front">
    <div class="front-brand">
      <span class="front-brand__dot"></span>
      <span class="front-brand__name">MorvaLeap</span>
    </div>
    <p class="front-url">www.lumoraflow.org</p>
  </section>

  <section class="card card--back">
    <svg class="back-wave" viewBox="0 0 700 400" width="700" height="400">
      <path d="M0,0 H700 V20 C700,90 660,120 560,140 C420,168 260,170 150,195 C80,212 45,240 40,290 V0 Z" fill="var(--navy)"/>
      <path d="M0,0 H40 V290 C45,240 80,212 150,195 C260,170 420,168 560,140 C660,120 700,90 700,20" fill="none"/>
      <path d="M700,35 C698,110 660,135 560,153 C420,180 260,182 150,206 C85,222 52,250 48,300" fill="none" stroke="var(--red)" stroke-width="4"/>
      <path d="M0,0 V400" stroke="var(--navy)" stroke-width="0"/>
    </svg>
    <div class="holder">
      <p class="holder__name">JONAH PELLERIN</p>
      <p class="holder__title">PRESIDENT</p>
    </div>
    <div class="back-brand">
      <span class="back-brand__dot"></span>
      <span class="back-brand__name">Lumora Flow Collective</span>
    </div>
    <div class="address">
      <p>412 Willowbend Court</p>
      <p>Cedar Falls, Oregon 97321</p>
      <p>www.lumoraflow.org</p>
    </div>
    <ul class="contacts">
      <li><svg viewBox="0 0 16 16"><path d="M3 1l3 3-2 2c1 2 3 4 5 5l2-2 3 3-2 3C7 15 1 9 1 3z"/></svg>555-204-7813</li>
      <li><svg viewBox="0 0 16 16"><path d="M4 0h8v16H4zM5.5 2v10h5V2z"/></svg>555-318-6092</li>
      <li><svg viewBox="0 0 16 16"><path d="M4 1h8v4H4zM1 6h14v7H1zM4 11h8v4H4z"/></svg>555-427-1950</li>
      <li><svg viewBox="0 0 16 16"><path d="M1 3h14v10H1zM2 4l6 5 6-5v-.5H2z"/></svg>hello@lumoraflow.org</li>
    </ul>
  </section>
</body>
</html>
```